Business Cards for Marco and Tobin

Design of business cards for two people with the recently created brand Valcor Mobile. Valcor Mobile wants to become a worldwide major player on the secondhand phone market. It gathers send hand phones from individuals, refurbish them and sell them throughout the world. It has a green impact (recycling) and we also contribute to social project in Africa (a percentage of our benefits are sent to build school, sport facilities, etc.

Target Market(s)

B2B - Marco and Tobin are in contact with distributors across Africa.

Industry/Entity Type

Wireless Communication

Contact Information for Business Card

Marco Feuillet
Head of Emerging Markets
Valcor Energy South Africa (Pty) Ltd
Kestrel Road 47
2031 Sandton - Johannesburg
South Africa
Tel: + 27 10 555 0148
Mobile : +27 82 55 104
Email : marco.feuillet@valcormobile.example
Skype: marco.feuillet
Web: www.valcormobile.example
 

Tobin Farrow
Head of Southern Africa
Kestrel Road 47
South Africa
Tel: + 27 10 555 0148
Mobile: +27 83 555 0276
Email: tobin.farrow@valcormobile.example
Skype: tobin.farrow
Web: www.valcormobile.example

Requirements
Must have
• The cards need to be "serious", trustable, with a worldwide presence.
Nice to have
• Some "green" / recycling touch would be nice but not necessary if in contradiction with the general design.

```html
<!DOCTYPE html>
<html lang="en">
<head>
<meta charset="utf-8">
<title>Valcor Mobile – Business Card, Marco Feuillet</title>
<link rel="stylesheet" href="https://fonts.googleapis.com/css2?family=Catamaran:wght@400;500;600&display=swap">
<style>
  :root {
    --page-bg: #ececec;
    --card-bg: #ffffff;
    --ink: #2b2b2b;
    --ink-soft: #333333;
    --bar: #333333;
    --brand-blue: #3797dc;
    --brand-navy: #2c3e50;
  }
  * { margin: 0; padding: 0; box-sizing: border-box; }
  html, body {
    width: 1200px;
    height: 1000px;
    overflow: hidden;
    background: var(--page-bg);
    font-family: "Catamaran", sans-serif;
  }
  .card {
    position: absolute;
    left: 352px;
    top: 80px;
    width: 496px;
    height: 320px;
    background: var(--card-bg);
    overflow: hidden;
  }
  .holder { position: absolute; left: 37px; top: 50px; }
  .holder-name {
    font-size: 19px;
    font-weight: 400;
    color: var(--ink);
    line-height: 24px;
    letter-spacing: 0.1px;
  }
  .holder-role {
    font-size: 11.5px;
    color: var(--brand-blue);
    line-height: 13px;
  }
  .divider {
    position: absolute;
    top: 92px;
    height: 8px;
    background: var(--bar);
  }
  .divider--left { left: 0; width: 324px; }
  .divider--right { left: 468px; width: 28px; }
  .brand-mark {
    position: absolute;
    left: 378px;
    top: 18px;
    width: 14px;
    height: 14px;
    background: var(--brand-blue);
  }
  .brand-name {
    position: absolute;
    left: 332px;
    top: 81px;
    width: 130px;
    text-align: center;
    font-size: 18px;
    font-weight: 600;
    color: var(--brand-navy);
    line-height: 26px;
    white-space: nowrap;
  }
  .address {
    position: absolute;
    left: 37px;
    top: 124px;
    font-size: 12.5px;
    line-height: 18px;
    color: var(--ink-soft);
    list-style: none;
  }
  .contacts {
    position: absolute;
    left: 19px;
    top: 208px;
    list-style: none;
    font-size: 12.5px;
    line-height: 18px;
    color: var(--ink-soft);
  }
  .contacts li { display: flex; align-items: center; height: 18px; }
  .contacts svg { width: 12px; height: 12px; margin-right: 6px; flex: none; }
  .corner-graphic {
    position: absolute;
    right: 0;
    bottom: 0;
    width: 158px;
    height: 172px;
  }
</style>
</head>
<body>
  <article class="card">
    <header class="holder">
      <h1 class="holder-name">Marco Feuillet</h1>
      <p class="holder-role">Head of Emerging Markets</p>
    </header>

    <span class="brand-mark" aria-hidden="true"></span>
    <div class="divider divider--left"></div>
    <p class="brand-name">Valcor Mobile</p>
    <div class="divider divider--right"></div>

    <ul class="address">
      <li>Valcor Energy South Africa (Pty) Ltd</li>
      <li>Kestrel Road 47</li>
      <li>2031 Sandton - Johannesburg</li>
      <li>South Africa</li>
    </ul>

    <ul class="contacts">
      <li>
        <svg viewBox="0 0 12 12" aria-hidden="true"><circle cx="6" cy="6" r="6" fill="var(--brand-blue)"/><path d="M3.6 3.2l1.2-.4.8 1.6-.7.6c.4.9 1 1.5 1.9 1.9l.6-.7 1.6.8-.4 1.2C6 8.4 3.6 6 3.6 3.2z" fill="#fff"/></svg>
        + 27 10 555 0148
      </li>
      <li>
        <svg viewBox="0 0 12 12" aria-hidden="true"><circle cx="6" cy="6" r="6" fill="var(--brand-blue)"/><rect x="4" y="2.6" width="4" height="6.8" rx="0.8" fill="#fff"/><rect x="4.6" y="3.4" width="2.8" height="4.4" fill="var(--brand-blue)"/></svg>
        + 27 82 55 104
      </li>
      <li>
        <svg viewBox="0 0 12 12" aria-hidden="true"><circle cx="6" cy="6" r="6" fill="var(--brand-blue)"/><circle cx="6" cy="6" r="3" fill="#fff"/></svg>
        marco.feuillet
      </li>
      <li>
        <svg viewBox="0 0 12 12" aria-hidden="true"><circle cx="6" cy="6" r="6" fill="var(--brand-blue)"/><rect x="3" y="3.8" width="6" height="4.4" fill="#fff"/><path d="M3 3.8l3 2.4 3-2.4" stroke="var(--brand-blue)" stroke-width="0.8" fill="none"/></svg>
        marco.feuillet@valcormobile.example
      </li>
      <li>
        <svg viewBox="0 0 12 12" aria-hidden="true"><circle cx="6" cy="6" r="6" fill="var(--brand-blue)"/><circle cx="6" cy="6" r="3.3" fill="none" stroke="#fff" stroke-width="0.8"/><path d="M2.7 6h6.6M6 2.7v6.6" stroke="#fff" stroke-width="0.8"/></svg>
        www.valcormobile.example
      </li>
    </ul>

    <svg class="corner-graphic" viewBox="0 0 158 172" role="img" aria-label="Brand graphic area in blue">
      <polygon points="158,0 158,172 0,172" fill="var(--brand-blue)"/>
    </svg>
  </article>
</body>
</html>
```